Internal Web Pages for Metrivane Labs

I need internal web pages (Why Metrivane Labs?, What We Offer, Blog, Testimonials) that match the design of the homepage. These do not need to be as long or in-depth as the landing page (provided for reference) but I will need three, maybe four, total pages (I'll select the max number of pages for now, but these will all be simple and short pages). Also attached is our new logo design for the company.

They are to essentially be:
Why Metrivane Labs? - An About Us and Why Choose Us page rolled into one.
What We Offer - A Services type page
Blog - self-explanatory
Testimonials - Customer Reviews and Use Cases

Also, maybe a very simple "Contact Us" page as well.

Target Market(s)

Business professionals that work with data analytics teams

Industry/Entity Type

Data Science

Number of Pages Required

5+ page

Requirements
Must have
• It must match the original design in theme and colors.
Nice to have
• Simple pages that show continuity that flows from the original landing page.
Should not have
• Can not be a different design that does not match the landing page.

```html
<!DOCTYPE html>
<html lang="en">
<head>
<meta charset="utf-8">
<title>Contact — Metrivane Labs</title>
<link href="https://fonts.googleapis.com/css2?family=Poppins:wght@300;400;600&family=Raleway:wght@400&family=Roboto:wght@400;500;700&display=swap" rel="stylesheet">
<style>
:root{
  --accent:#5c6ae8;
  --orange:#f08300;
  --ink:#2b2b2b;
  --muted:#5a5a5a;
  --line:#dcdcdc;
  --map-light:#e6e6e6;
  --map-mid:#d3d3d3;
  --footer:#18073f;
  --footer-base:#130432;
  --white:#ffffff;
}
*{margin:0;padding:0;box-sizing:border-box}
html,body{width:1200px;height:2198px;overflow:hidden;background:var(--white)}
body{position:relative;font-family:"Raleway",sans-serif;color:var(--ink)}
/* header */
.site-header{position:absolute;left:0;top:0;width:1200px;height:87px;background:var(--white)}
.brand{position:absolute;display:flex;align-items:center;gap:8px;font-family:"Poppins",sans-serif;font-weight:300;color:var(--accent);font-size:36px;letter-spacing:.5px;white-space:nowrap}
.brand-dot{width:30px;height:30px;background:var(--accent)}
.site-header .brand{left:94px;top:18px}
.nav{position:absolute;top:31px;font-family:"Poppins",sans-serif;font-size:16px;color:#555}
.nav.active{color:var(--accent)}
.btn-start{position:absolute;left:976px;top:23px;width:131px;height:39px;background:var(--orange);color:#fff;font-family:"Poppins",sans-serif;font-weight:600;font-size:13px;letter-spacing:.6px;display:flex;align-items:center;justify-content:center;box-shadow:0 4px 10px rgba(240,131,0,.35)}
/* hero */
.hero{position:absolute;left:0;top:87px;width:1200px;height:362px}
.hero-title{position:absolute;left:84px;top:93px;font-family:"Poppins",sans-serif;font-weight:400;font-size:41px;color:#fff}
.hero-sub{position:absolute;left:86px;top:148px;font-family:"Roboto",sans-serif;font-size:16px;color:#fff}
/* contact card */
.card-back{position:absolute;left:239px;top:670px;width:317px;height:376px;background:#fff;box-shadow:0 2px 10px rgba(0,0,0,.12)}
.card{position:absolute;left:145px;top:562px;width:390px;height:462px;background:#fff;box-shadow:0 2px 12px rgba(0,0,0,.14)}
.info-icon{position:absolute;left:39px}
.info-title{position:absolute;left:112px;font-family:"Poppins",sans-serif;font-size:24px;color:#222}
.info-text{position:absolute;left:112px;font-size:16px;line-height:25px;color:var(--muted);width:270px}
.info-rule{position:absolute;left:39px;width:320px;border-top:1px dotted #d8d8d8}
/* form */
.form-heading{position:absolute;left:609px;top:578px;font-family:"Poppins",sans-serif;font-weight:300;font-size:39px;line-height:43px;color:#222}
.heading-rule{position:absolute;left:612px;top:690px;width:142px;height:2px;background:var(--accent)}
.field-label{position:absolute;font-family:"Poppins",sans-serif;font-size:19px;color:#444}
.field-line{position:absolute;height:1px;background:var(--line)}
.btn-send{position:absolute;left:609px;top:991px;width:176px;height:49px;background:var(--orange);color:#fff;font-family:"Roboto",sans-serif;font-weight:700;font-size:15px;display:flex;align-items:center;justify-content:center;gap:8px}
/* map */
.map{position:absolute;left:0;top:1150px;width:1200px;height:481px}
/* footer */
.footer{position:absolute;left:0;top:1630px;width:1200px;height:431px;background:var(--footer);font-family:"Roboto",sans-serif;color:#fff}
.footer .brand{left:143px;top:106px;color:var(--accent);font-size:35px}
.footer .brand-dot{width:28px;height:28px}
.footer-about{position:absolute;left:143px;top:177px;width:290px;font-size:15.5px;line-height:22px}
.social{position:absolute;top:298px;width:36px;height:36px;border:1.5px solid #fff;border-radius:50%}
.footer-h{position:absolute;font-weight:700;font-size:19px;letter-spacing:.3px}
.footer-item{position:absolute;left:517px;font-weight:500;font-size:16px;line-height:21px;letter-spacing:.6px}
.footer-icon{position:absolute;left:480px}
.footer-note{position:absolute;left:754px;top:159px;width:310px;font-size:14.5px;line-height:24px}
.email-input{position:absolute;left:754px;top:218px;width:303px;height:39px;background:#fff;color:#666;font-size:14px;padding:0 18px;display:flex;align-items:center}
.btn-sub{position:absolute;left:754px;top:273px;width:126px;height:39px;background:var(--orange);font-weight:700;font-size:14.5px;display:flex;align-items:center;justify-content:center}
.footer-base{position:absolute;left:0;top:2061px;width:1200px;height:137px;background:var(--footer-base);font-family:"Roboto",sans-serif;color:#fff;font-size:16px;font-weight:500;text-align:center;padding-top:66px}
</style>
</head>
<body>

<header class="site-header">
  <div class="brand"><span class="brand-dot"></span>MetrivaneLabs</div>
  <span class="nav" style="left:467px">Home</span>
  <span class="nav" style="left:550px">About us</span>
  <span class="nav" style="left:658px">Our Service</span>
  <span class="nav" style="left:787px">Blog</span>
  <span class="nav active" style="left:856px">Contact</span>
  <span class="btn-start">GET STARTED</span>
</header>

<section class="hero">
  <svg width="1200" height="362" viewBox="0 0 1200 362" role="img" aria-label="Photo of a hand holding a glowing blue phone icon beside a man in a suit">
    <defs>
      <linearGradient id="heroGrad" x1="0" y1="0" x2="1" y2="0">
        <stop offset="0" stop-color="#000"/>
        <stop offset=".55" stop-color="#07090f"/>
        <stop offset=".8" stop-color="#3a3531"/>
        <stop offset="1" stop-color="#8a6f52"/>
      </linearGradient>
      <radialGradient id="glow" cx=".55" cy=".35" r=".18">
        <stop offset="0" stop-color="#1f6fd6" stop-opacity=".55"/>
        <stop offset="1" stop-color="#1f6fd6" stop-opacity="0"/>
      </radialGradient>
    </defs>
    <polygon points="120,278 414,362 1000,274" fill="var(--accent)"/>
    <polygon points="0,0 1200,0 1200,250 414,345 0,253" fill="url(#heroGrad)"/>
    <polygon points="0,0 1200,0 1200,250 414,345 0,253" fill="url(#glow)"/>
  </svg>
  <h1 class="hero-title">Contact</h1>
  <p class="hero-sub">Fill In the Form for information or a meeting!</p>
</section>

<div class="card-back"></div>
<div class="card">
  <svg class="info-icon" style="top:68px" width="52" height="48" viewBox="0 0 52 48">
    <path d="M0 18 L14 12 L26 18 L38 12 L52 18 L52 46 L38 40 L26 46 L14 40 L0 46Z" fill="var(--accent)"/>
    <path d="M26 0a11 11 0 0 1 11 11c0 8-11 20-11 20S15 19 15 11A11 11 0 0 1 26 0z" fill="var(--accent)" stroke="#fff" stroke-width="2"/>
    <circle cx="26" cy="11" r="4" fill="#fff"/>
  </svg>
  <div class="info-title" style="top:74px">Location</div>
  <div class="info-text" style="top:109px">48 Fenwick Row, Harlow Quay, United Kingdom, HQ4 7RT</div>
  <div class="info-rule" style="top:187px"></div>

  <svg class="info-icon" style="top:227px" width="46" height="46" viewBox="0 0 24 24">
    <path d="M20 15.5c-1.2 0-2.4-.2-3.6-.6a1 1 0 0 0-1 .25l-2.2 2.2a15 15 0 0 1-6.6-6.6l2.2-2.2a1 1 0 0 0 .25-1A11.4 11.4 0 0 1 8.5 4a1 1 0 0 0-1-1H4a1 1 0 0 0-1 1 17 17 0 0 0 17 17 1 1 0 0 0 1-1v-3.5a1 1 0 0 0-1-1z" fill="var(--accent)" transform="scale(-1,1) translate(-24,0)"/>
  </svg>
  <div class="info-title" style="top:226px">Make a Call</div>
  <div class="info-text" style="top:259px">+44-20-5550-1382</div>
  <div class="info-rule" style="top:315px"></div>

  <svg class="info-icon" style="top:350px" width="46" height="44" viewBox="0 0 46 44">
    <path d="M2 18 L23 2 L44 18 L44 42 L2 42Z" fill="var(--accent)"/>
    <path d="M10 24 L23 34 L36 24" fill="none" stroke="#fff" stroke-width="3" stroke-linecap="round"/>
  </svg>
  <div class="info-title" style="top:345px">Send a Mail</div>
  <div class="info-text" style="top:376px">hello@metrivanelabs.com</div>
</div>

<h2 class="form-heading">We’d love to hear from<br>you anytime</h2>
<div class="heading-rule"></div>
<span class="field-label" style="left:610px;top:725px">Name</span>
<div class="field-line" style="left:607px;top:766px;width:448px"></div>
<span class="field-label" style="left:610px;top:784px">Email</span>
<div class="field-line" style="left:607px;top:828px;width:204px"></div>
<span class="field-label" style="left:830px;top:784px">Phone</span>
<div class="field-line" style="left:828px;top:828px;width:227px"></div>
<span class="field-label" style="left:609px;top:851px">Tell us about project</span>
<div class="field-line" style="left:607px;top:976px;width:448px"></div>
<span class="btn-send">SEND MESSAGE
  <svg width="14" height="12" viewBox="0 0 14 12"><path d="M1 6h11M7 1l5 5-5 5" fill="none" stroke="#fff" stroke-width="2.2"/></svg>
</span>

<div class="map">
  <svg width="1200" height="481" viewBox="0 0 1200 481" role="img" aria-label="Street map showing the office location">
    <defs>
      <linearGradient id="mapGrad" x1="0" y1="0" x2="1" y2="0">
        <stop offset="0" stop-color="var(--map-light)"/>
        <stop offset=".5" stop-color="var(--map-mid)"/>
        <stop offset="1" stop-color="var(--map-light)"/>
      </linearGradient>
    </defs>
    <polygon points="120,84 414,2 1000,88" fill="var(--accent)"/>
    <polygon points="0,105 414,17 1200,112 1200,481 0,481" fill="url(#mapGrad)"/>
  </svg>
</div>

<footer class="footer">
  <div class="brand"><span class="brand-dot"></span>MetrivaneLabs</div>
  <p class="footer-about">Sed ut perspiciatis unde omnis iste natus error sit voluptatem accusantium dolorque laudantium, totam rem aperiam, eaque ipsa quae ab illo inventore veritatis et quasi</p>
  <span class="social" style="left:145px" aria-label="Social profile"></span>
  <span class="social" style="left:186px" aria-label="Social profile"></span>
  <span class="social" style="left:227px" aria-label="Social profile"></span>
  <span class="social" style="left:268px" aria-label="Social profile"></span>

  <div class="footer-h" style="left:480px;top:113px">CONTACT US</div>
  <svg class="footer-icon" style="top:159px" width="18" height="24" viewBox="0 0 18 24"><path d="M9 1a8 8 0 0 1 8 8c0 6-8 14-8 14S1 15 1 9a8 8 0 0 1 8-8z" fill="none" stroke="#fff" stroke-width="1.5"/><circle cx="9" cy="9" r="3" fill="none" stroke="#fff" stroke-width="1.5"/></svg>
  <div class="footer-item" style="top:164px">Metrivane Labs<br>250 ipsam voluptatem<br>quia voluptas</div>
  <svg class="footer-icon" style="top:244px" width="20" height="20" viewBox="0 0 24 24"><path d="M20 15.5c-1.2 0-2.4-.2-3.6-.6a1 1 0 0 0-1 .25l-2.2 2.2a15 15 0 0 1-6.6-6.6l2.2-2.2a1 1 0 0 0 .25-1A11.4 11.4 0 0 1 8.5 4a1 1 0 0 0-1-1H4a1 1 0 0 0-1 1 17 17 0 0 0 17 17 1 1 0 0 0 1-1v-3.5a1 1 0 0 0-1-1z" fill="none" stroke="#fff" stroke-width="1.4"/></svg>
  <div class="footer-item" style="top:246px">Phone :<br>555-0142-7730</div>
  <svg class="footer-icon" style="top:311px" width="21" height="15" viewBox="0 0 21 15"><rect x=".75" y=".75" width="19.5" height="13.5" fill="none" stroke="#fff" stroke-width="1.4"/><path d="M1 1l9.5 8L20 1" fill="none" stroke="#fff" stroke-width="1.4"/></svg>
  <div class="footer-item" style="top:309px">Email :<br>info@metrivanelabs.com</div>

  <div class="footer-h" style="left:754px;top:110px">SIGN UP TO RECEIVE EMAIL</div>
  <p class="footer-note">Excepteur sint occaecat cupidatat non proi-<br>dent, sunt in culpa qui Nemo enim ipsam vo-</p>
  <div class="email-input">Enter Email</div>
  <span class="btn-sub">SUBSCRIBE</span>
</footer>

<div class="footer-base">Copyright © Metrivane Labs 2021. All rights reserved. | Privacy Policy</div>

</body>
</html>
```